Contractor Plan "B"/Getting Screwed?/Something Useful

We are sending out a series of postcards to a group of local contractors.

The first in the series is: Plan B: Pink Bubble Wrap. Plan A is to buy insurance from my agency. This will be printed, front and back on card stock. We will then glue a piece of bubble wrap to the card and place it in an envelope for delivery.

The second card will be along the same lines but will ask if the client is getting screwed by his current Insurance Company. We will glue a screw in the middle of the card and place the card in an envelope for delivery. On the bottom of we might tell them to call us to get unscrewed.

The third card will follow those lines but say something like: We sent you bubble wrap for your Plan B and you didn't call. Then we sent you something funny but you didn't call. We decided to send you something useful so you might call now! With this card, we are going to send a carpenter pencil.

I am attaching a rough outline of my sketch design for the first card so you will have basic information we will need such as phone number and coverages we offer. If you feel like there is too much info for the size of the card, we can leave some off. I just want the phone to ring! Also, feel free to adjust the wording to make it work better...creative design is not my strong suit!!

I would like for all three cards to be designed. Each can have the same backside. Also, please keep in mind, this is not a postcard so you don't have to leave the blanks on the back for addressing. Each will be mailed in an envelope.

I have also uploaded my logo file as we have recently redone the logo.
Updates

Here is more guidance on the project: The cards are going to be 10 cm wide and 23 cm tall. I have added more wording in the brief. Also, I attached a word doc with a good idea of what to use for wording. Basically I want the following idea: Card 1: At top of card - Plan B: Pink Bubble Wrap Below the bubble wrap - Plan A: Call us so you don't have to use Pink Bubble Wrap Card 2: At top of card - Getting Screwed? Is your current agent taking you for granted? Below the area where we are going to glue a screw - Get unscrewed, Call us! Card 3: At top of card - We have the sharpest pencil in town! We will leave space for a carpenter pencil to be attached tot he card. On the other side of the open space - Call us today for the best rates on your insurance!

Please review the attached word doc for an idea of what to put on the back of the card. To be clear, we need three designs for the front of the card and can probably use just one design for the back of all three. If you think we need to have a different design for the back of each, I would like to see your ideas. Thank you for your hard work on these!

Reason: Hi, I am extending the time as I am expecting a few more submissions. Thank you!

Target Market(s)

We are targeting both contractors and truckers with this campaign.

Industry/Entity Type

Insurance

Requirements
Must have
• Clever wording. It needs to be a call to action and doesn't need to have too many specifics.

We also have to have space in the middle to glue the bubble wrap on the first card, the screw in the second and attach the pencil in the third.

```html
<!DOCTYPE html>
<html lang="en">
<head>
<meta charset="utf-8">
<title>Contractor Card Series – Plan B, Getting Screwed, Something Useful</title>
<link rel="stylesheet" href="https://fonts.googleapis.com/css2?family=Roboto+Condensed:wght@400;700&family=Allura&display=swap">
<style>
  :root{
    --stage:#2f2925;
    --card-frame:#f7f7f7;
    --top-grey:#e4e4e6;
    --band-grey:#9c9c9e;
    --brand-red:#b3131c;
    --deep-red:#8f0f16;
    --ink:#1d1d1d;
    --ink-soft:#444;
    --white:#ffffff;
    --pink-script:#d431cf;
    --phone-mute:#e9d3d3;
    --slot-border:#a8a8a8;
  }
  *{box-sizing:border-box;margin:0;padding:0}
  html,body{width:1200px;height:450px;overflow:hidden;background:var(--stage)}
  .card-series{
    width:1200px;height:450px;
    display:flex;justify-content:space-evenly;align-items:center;
    font-family:"Roboto Condensed",Arial,sans-serif;
  }
  .card{
    width:196px;height:426px;
    background:var(--card-frame);
    padding:8px;
    box-shadow:0 4px 14px rgba(0,0,0,.45);
  }
  .card-panel{
    position:relative;width:100%;height:100%;overflow:hidden;
    background:linear-gradient(var(--top-grey) 0 47%, var(--brand-red) 47% 100%);
    text-align:center;color:var(--white);
  }
  .grey-band{
    position:absolute;left:0;right:0;top:calc(47% - 9px);height:9px;
    background:var(--band-grey);
  }
  .object-slot{
    position:absolute;left:50%;top:128px;transform:translateX(-50%);
    width:104px;height:104px;background:var(--white);
    border:3px solid var(--slot-border);padding:5px;
  }
  .object-fill{width:100%;height:100%}
  .fill-bubble{background:radial-gradient(circle at 40% 40%,#f6d3e4,#d99bbb 70%,#c781a6)}
  .fill-screw{background:linear-gradient(135deg,#ffffff,#d8dadc 45%,#9ea3a8 60%,#f2f2f2)}
  .fill-pencil{background:linear-gradient(135deg,#ffffff 0 35%,#f1c232 45%,#e0a21a 60%,#ffffff 70%)}
  .headline{
    position:absolute;left:0;right:0;top:40px;
    font-weight:700;font-size:25px;color:var(--ink);line-height:1;
  }
  .script-line{
    position:absolute;left:0;right:0;top:70px;
    font-family:"Allura",cursive;font-size:25px;color:var(--pink-script);
  }
  .question{
    position:absolute;left:0;right:0;top:36px;
    font-weight:700;font-size:19px;color:var(--ink);
  }
  .subquestion{
    position:absolute;left:18px;right:18px;top:64px;
    font-size:11px;color:var(--ink-soft);line-height:1.25;
  }
  .story{
    position:absolute;left:12px;right:12px;top:22px;
    font-weight:700;font-size:10.5px;color:var(--ink);line-height:1.2;
  }
  .story p{margin-bottom:6px}
  .call-line{
    position:absolute;left:14px;right:14px;top:268px;
    font-size:11px;line-height:1.35;
  }
  .call-line.strong{font-size:11.5px}
  .phone{
    position:absolute;left:0;right:0;top:354px;
    font-weight:700;font-size:19px;letter-spacing:.3px;
  }
  .phone.muted{color:var(--phone-mute)}
  .call-above{
    position:absolute;left:0;right:0;top:338px;font-weight:700;font-size:11px;color:var(--phone-mute);
  }
  .fine-print{
    position:absolute;left:6px;right:6px;top:384px;
    font-size:5.6px;font-weight:700;
  }
  /* back side */
  .brand-mark{
    position:absolute;left:0;right:0;top:8px;
    display:flex;justify-content:center;align-items:center;gap:5px;
    font-weight:700;font-size:14px;color:var(--deep-red);
  }
  .brand-mark .mark-square{width:9px;height:9px;background:var(--deep-red)}
  .brand-name{
    position:absolute;left:0;right:0;top:30px;
    font-weight:700;font-size:13.5px;color:var(--ink);
  }
  .coverage-collage{
    position:absolute;left:0;right:0;top:56px;height:186px;
    background:linear-gradient(160deg,#9fb7cf,#c9b08f 50%,#6f7f8d);
  }
  .coverage-intro{
    position:absolute;left:0;right:0;top:252px;
    font-weight:700;font-size:9.5px;line-height:1.25;
  }
  .coverage-list{list-style:none}
  .promise{
    position:absolute;left:10px;right:10px;top:312px;
    font-weight:700;font-size:8px;line-height:1.2;
  }
  .back .phone{top:340px;font-size:22px}
  .web{position:absolute;left:0;right:0;top:368px;font-weight:700;font-size:10px}
  .street{position:absolute;left:0;right:0;top:394px;font-size:6.5px}
</style>
</head>
<body>
<main class="card-series">

  <article class="card front plan-b">
    <div class="card-panel">
      <h1 class="headline">Plan B</h1>
      <div class="script-line">Pink Bubble Wrap</div>
      <div class="grey-band"></div>
      <div class="object-slot"><div class="object-fill fill-bubble" role="img" aria-label="Square of pink bubble wrap glued to the card"></div></div>
      <p class="call-line">Call us so you don't have to use<br>Pink Bubble Wrap</p>
      <p class="phone">555-014-2270</p>
      <p class="fine-print">Why pink?&nbsp; You might not get sued if they think you are a wuss.</p>
    </div>
  </article>

  <article class="card back">
    <div class="card-panel">
      <div class="brand-mark"><span class="mark-square"></span>RIG</div>
      <h2 class="brand-name">Ridgeline Insurance Group</h2>
      <div class="coverage-collage" role="img" aria-label="Collage of snapshots: luxury car, yacht, trucks, a house, an airplane, construction workers and a healthcare scene"></div>
      <div class="coverage-intro">
        <p>Your Source For All Things Insurance</p>
        <ul class="coverage-list">
          <li>• Builders Risk • Property</li>
          <li>• Workers Compensation</li>
          <li>General Liability • Flood • Health</li>
        </ul>
      </div>
      <p class="promise">Our job is to make sure you can sleep at night. Call us today to get the best rates from multiple insurance carriers.</p>
      <p class="phone">555-014-2270</p>
      <p class="web">www.ridgelineinsure.com</p>
      <p class="street">4810 Cedar Hollow Rd, Maple Falls, Texas 77001</p>
    </div>
  </article>

  <article class="card front screwed">
    <div class="card-panel">
      <h1 class="question">Getting Screwed?</h1>
      <p class="subquestion">Is your current agent<br>taking you for granted?</p>
      <div class="grey-band"></div>
      <div class="object-slot"><div class="object-fill fill-screw" role="img" aria-label="Metal screw glued to the card"></div></div>
      <p class="call-line strong">Get unscrewed<br>Call us!</p>
      <p class="phone">555-014-2270</p>
      <p class="fine-print">Why pink?&nbsp; You might not get sued if they think you are a wuss.</p>
    </div>
  </article>

  <article class="card front useful">
    <div class="card-panel">
      <div class="story">
        <p>We sent some bubble wrap,<br>you didn't call.</p>
        <p>We offered to unscrew you and<br>we didn't hear back.</p>
        <p>Now, we are sending something<br>useful hoping you will call!</p>
      </div>
      <div class="grey-band"></div>
      <div class="object-slot"><div class="object-fill fill-pencil" role="img" aria-label="Yellow pencil attached to the card"></div></div>
      <p class="call-above">Call us!</p>
      <p class="phone muted">555-014-2270</p>
      <p class="fine-print">Why pink?&nbsp; You might not get sued if they think you are a wuss.</p>
    </div>
  </article>

</main>
</body>
</html>
```